Suds Harbor Laundromat Wordpress Design

We need a Wordpress website design for our laundromat, Suds Harbor Atlanta, at www.sudsharboratlanta-example.com. We would like to have 6 pages: Home, About Us, Services, Locations, Reviews and Contact us. We will provide content for the text on each page. What we do: We are a full service laundromat that provides dry cleaning drop off, professional laundry services, wash dry fold and self service laundry to the local community. We would like to use the color scheme from our logo to convey a warm, safe, and bright business that caters to its diverse community.
Updates

I like the structure of this laundromat website: http://www.tumblewashhub-example.com/ Using my logo and color scheme in the above referenced website is what. Am looking for. The photos attached to the project with the female model should be used as a primary focus and supplemented by actual photos of the equipment.

Target Market(s)

Our target market is a diverse group of people from Midtown Atlanta - LGBTQ community /Locals/Regulars that have been coming to laundromat for 30 years.

Industry/Entity Type

Laundromat

Coding

Coded - Design and coding required

Number of Pages Required

5+ page

Font styles to use
Sans Serif

Colors
0054AA
0677BA
7BADD7
CADEEF
E8F1F8

Requirements
Must have
• Feature this video on the main page: https://video.example.com/Qx7mBr2Lp0Z

```html
<!DOCTYPE html>
<html lang="en">
<head>
<meta charset="utf-8">
<title>Suds Harbor Atlanta – Full Service Laundromat</title>
<link href="https://fonts.googleapis.com/css2?family=Oswald:wght@300;400;500;600&family=Poppins:wght@400;500;600;700&display=swap" rel="stylesheet">
<style>
:root{
  --navy:#0a4c9e;
  --blue:#0a5cb4;
  --royal:#0d62c0;
  --sky:#1e9cf0;
  --cyan:#19c6f5;
  --ink:#444a55;
  --muted:#8a8f99;
  --line:#e3e6ea;
  --white:#ffffff;
  --gold:#f3b431;
  --footer:#0b4899;
}
*{margin:0;padding:0;box-sizing:border-box}
html,body{width:1200px;height:4260px;overflow:hidden;background:var(--white)}
body{font-family:'Poppins',sans-serif;color:var(--ink);position:relative}
.page{position:relative;width:1200px;height:4260px;overflow:hidden}
.abs{position:absolute}
.heading{font-family:'Oswald',sans-serif;font-weight:300;color:var(--navy);text-transform:uppercase;letter-spacing:-.2px}
.sub{font-family:'Oswald',sans-serif;font-weight:400;text-transform:uppercase;font-size:14px;color:var(--navy);letter-spacing:-.1px}
.para{font-size:14px;line-height:24px;color:var(--ink)}
.btn{position:absolute;display:flex;align-items:center;justify-content:center;border-radius:22px;font-size:11px;font-weight:600;text-transform:uppercase;letter-spacing:.2px;text-decoration:none}
.btn-solid{background:var(--sky);color:var(--white)}
.btn-outline{border:2px solid var(--navy);color:var(--sky);background:var(--white)}
.btn-white{background:var(--white);color:var(--navy)}

/* header */
.site-header{position:absolute;left:0;top:0;width:1200px;height:88px;background:var(--white);z-index:5}
.brand{position:absolute;display:flex;align-items:center;gap:8px;font-family:'Oswald',sans-serif;font-weight:500;text-transform:uppercase}
.brand-dot{border-radius:50%;background:var(--cyan)}
.site-header .brand{left:92px;top:26px;font-size:28px;color:var(--navy)}
.site-header .brand-dot{width:12px;height:12px}
.nav{position:absolute;right:88px;top:0;display:flex;gap:23px;height:88px;align-items:center}
.nav a{font-family:'Oswald',sans-serif;font-size:15px;color:#333;text-decoration:none;text-transform:uppercase;position:relative;height:88px;display:flex;align-items:center}
.nav a.active{color:var(--sky)}
.nav a.active::before{content:"";position:absolute;top:0;left:-4px;right:-4px;height:4px;background:var(--sky)}

/* hero */
.hero-photo{left:0;top:88px;width:1200px;height:730px;background:linear-gradient(100deg,#5e5a52 0%,#c9c2b4 30%,#e2ddd2 55%,#bfb8aa 80%,#6c665c 100%)}
.hero-title{left:76px;top:360px;font-family:'Oswald',sans-serif;font-weight:600;font-size:53px;line-height:57px;color:var(--white);text-transform:uppercase}
.hero-tag{left:76px;top:546px;font-family:'Oswald',sans-serif;font-weight:300;font-size:19px;color:var(--white);text-transform:uppercase}
.play{left:150px;top:626px;width:72px;height:72px;border-radius:50%;background:var(--white);display:flex;align-items:center;justify-content:center}

/* about */
.about-title{left:0;width:1200px;top:826px;text-align:center;font-size:40px}
.about-sub{left:0;width:1200px;top:876px;text-align:center}
.about-rule{left:580px;top:908px;width:40px;height:1px;background:#c8ccd2}
.about-text{left:220px;width:760px;top:926px;text-align:center}
.divider{left:88px;width:1024px;height:1px;background:var(--line)}

.services-title{left:0;width:1200px;top:1210px;text-align:center;font-size:40px}
.services-rule{left:580px;top:1266px;width:40px;height:2px;background:#c8ccd2}

.service-title{font-size:32px}
.service-body{width:400px}

/* testimonials */
.reviews-title{left:0;width:1200px;top:3160px;text-align:center;font-size:40px}
.review{position:absolute;top:3290px;width:330px;height:213px;background:var(--white);box-shadow:0 4px 24px rgba(20,40,80,.09)}
.avatar{position:absolute;left:36px;top:-36px;width:72px;height:72px;border-radius:50%;background:linear-gradient(160deg,#b9a79a,#5d4d45)}
.quote{position:absolute;left:168px;top:-10px;font-family:Georgia,serif;font-size:110px;color:#eceef1;line-height:1}
.review-text{position:absolute;left:26px;top:68px;width:280px;font-size:13.5px;line-height:21px;color:var(--ink)}
.reviewer{position:absolute;left:26px;top:170px;font-size:14px;font-weight:700;color:var(--navy)}
.reviewer-place{position:absolute;left:26px;top:192px;font-size:11px;color:var(--muted)}
.stars{position:absolute;right:30px;top:172px;display:flex;gap:2px}

/* cta */
.cta-box{left:214px;top:3600px;width:772px;height:162px;background:var(--sky)}
.cta-text{position:absolute;left:70px;top:30px;font-family:'Oswald',sans-serif;font-weight:300;font-size:40px;line-height:46px;color:var(--white);text-transform:uppercase}

/* footer */
.footer-head{font-family:'Oswald',sans-serif;font-weight:500;font-size:19px;color:var(--white);text-transform:uppercase}
.footer-links{list-style:none}
.footer-links li{font-size:12px;color:var(--white);height:27px}
.footer-small{font-size:12px;line-height:22px;color:var(--white)}
.news-input{left:850px;top:4014px;width:260px;height:42px;background:var(--white);border-radius:21px;overflow:hidden}
.news-input span{position:absolute;left:36px;top:12px;font-size:12px;color:#555}
.news-send{position:absolute;right:0;top:0;width:42px;height:42px;background:var(--cyan);display:flex;align-items:center;justify-content:center}
.social{width:32px;height:32px;border-radius:50%;border:1px solid rgba(255,255,255,.5)}
.copyright{left:0;width:1200px;top:4226px;text-align:center;font-size:11px;font-weight:600;color:var(--white)}
.to-top{left:1136px;top:4184px;width:34px;height:34px;border-radius:50%;background:var(--white);display:flex;align-items:center;justify-content:center}
</style>
</head>
<body>
<div class="page">

<header class="site-header">
  <div class="brand"><span class="brand-dot"></span>Suds Harbor</div>
  <nav class="nav">
    <a class="active" href="#">Home</a>
    <a href="#">About Us</a>
    <a href="#">Services</a>
    <a href="#">Locations</a>
    <a href="#">Reviews</a>
    <a href="#">Contact Us</a>
  </nav>
</header>

<!-- hero -->
<div class="abs hero-photo" role="img" aria-label="Woman in a blue dress seated in front of a row of front-loading washers"></div>
<svg class="abs" style="left:0;top:88px" width="1200" height="740" viewBox="0 0 1200 740" aria-hidden="true">
  <defs>
    <linearGradient id="heroBlob" x1="0" y1="0" x2="1" y2="1">
      <stop offset="0" stop-color="#1ca8f2"/><stop offset="1" stop-color="#0e8fe6"/>
    </linearGradient>
  </defs>
  <path d="M0 690 C120 720 260 700 360 600 C430 520 480 420 488 320 C494 220 430 150 330 150 C220 150 150 210 60 190 C30 184 10 175 0 170 Z" fill="#19c6f5"/>
  <path d="M0 670 C120 700 250 680 345 585 C415 510 470 410 478 315 C484 220 420 160 330 160 C220 160 150 215 60 198 C30 192 10 183 0 178 Z" fill="url(#heroBlob)"/>
  <path d="M0 740 L0 708 C160 724 300 670 390 590 C450 535 520 560 600 570 C780 590 900 520 1000 460 C1080 412 1150 420 1200 430 L1200 740 Z" fill="#ffffff"/>
</svg>
<h1 class="abs hero-title">Laundromat,<br>Suds Harbor<br>Atlanta</h1>
<div class="abs hero-tag">A Full Service Laundromat</div>
<div class="abs play"><svg width="16" height="18" viewBox="0 0 16 18"><path d="M2 1 L15 9 L2 17 Z" fill="#0a4c9e"/></svg></div>

<!-- about -->
<h2 class="abs heading about-title">About Us</h2>
<div class="abs sub about-sub">Coin Laundry, Dry Cleaning, &amp; Professional Laundry</div>
<div class="abs about-rule"></div>
<p class="abs para about-text">Lorem quis bibendum auctor nisi elit consequat ipsum nec sagittis sem nibh id elit. Duis sed odio sit amet nibh vulputate cursus a sit amet mauris morbi accumsan ipsum velit nam nec tellus a tincidunt auctor a ornare odio sed non mauris vitae erat consequat</p>
<a class="btn btn-solid" style="left:534px;top:1022px;width:132px;height:40px">Read More</a>
<div class="abs divider" style="top:1131px"></div>

<!-- services -->
<h2 class="abs heading services-title">Suds Harbor Services</h2>
<div class="abs services-rule"></div>

<!-- coin laundry -->
<svg class="abs" style="left:86px;top:1296px" width="560" height="430" viewBox="0 0 560 430" aria-hidden="true">
  <path d="M300 425 C180 430 40 380 22 250 C40 330 140 400 270 408 Z" fill="#eceeef"/>
  <g fill="#d5d8dc">
    <circle cx="444" cy="40" r="4"/><circle cx="470" cy="40" r="4"/><circle cx="496" cy="40" r="4"/>
    <circle cx="444" cy="66" r="4"/><circle cx="470" cy="66" r="4"/><circle cx="496" cy="66" r="4"/>
    <circle cx="444" cy="92" r="4"/><circle cx="470" cy="92" r="4"/><circle cx="496" cy="92" r="4"/>
    <circle cx="496" cy="118" r="4"/>
  </g>
</svg>
<svg class="abs" style="left:86px;top:1296px" width="560" height="430" viewBox="0 0 560 430" role="img" aria-label="Row of front-loading washers with laundry carts in a laundromat">
  <defs><linearGradient id="coinPhoto" x1="0" y1="0" x2="1" y2="1"><stop offset="0" stop-color="#d8d2c2"/><stop offset=".5" stop-color="#a9a59b"/><stop offset="1" stop-color="#e7e3d8"/></linearGradient></defs>
  <path d="M270 4 C400 4 500 90 520 200 C535 280 545 340 545 402 C520 360 470 360 420 375 C380 392 330 400 270 398 C155 398 50 310 50 200 C50 90 155 4 270 4 Z" fill="url(#coinPhoto)"/>
  <path d="M44 120 C80 114 108 140 104 176 C100 205 76 220 46 216 C36 230 20 238 4 240 C16 228 22 214 18 200 C2 186 -4 160 8 142 C16 128 28 122 44 120 Z" fill="#19c6f5"/>
</svg>
<h3 class="abs heading service-title" style="left:710px;top:1346px">Coin Laundry Service</h3>
<div class="abs sub" style="left:712px;top:1388px">A Full Service Laundromat</div>
<p class="abs para service-body" style="left:712px;top:1422px">Lorem quis bibendum auctor nisi elit consequat ipsum nec sagittis sem nibh id elit. Duis sed odio sit amet nibh vulputate cursus a sit amet mauris morbi accumsan ipsum velit nam nec tellus a tincidunt...</p>
<a class="btn btn-outline" style="left:716px;top:1534px;width:134px;height:40px">Read More</a>

<!-- dry cleaning band -->
<svg class="abs" style="left:0;top:1690px" width="1200" height="940" viewBox="0 0 1200 940" aria-hidden="true">
  <defs>
    <linearGradient id="bandFill" x1="0" y1="0" x2="1" y2="1">
      <stop offset="0" stop-color="#0b55b0"/><stop offset="1" stop-color="#0a4a9e"/>
    </linearGradient>
  </defs>
  <path d="M0 250 C160 240 360 210 520 130 C700 40 860 -10 1040 10 C1120 18 1170 50 1200 80 L1200 860 C1050 880 900 780 700 770 C500 760 330 810 150 800 C80 796 30 780 0 760 Z" fill="url(#bandFill)"/>
  <path d="M150 800 C330 810 500 760 700 770 C650 750 550 745 450 760 C330 778 240 792 150 800 Z" fill="#19c6f5"/>
  <path d="M1040 10 C1120 18 1170 50 1200 80 L1200 95 C1160 60 1110 35 1040 10 Z" fill="#19c6f5"/>
  <path d="M0 70 C80 50 180 90 205 170 C225 240 190 290 120 295 C60 300 20 270 0 240 Z" fill="#7bb3de" opacity=".75"/>
  <path d="M1200 740 C1120 720 1020 760 970 820 C940 860 980 905 1060 910 C1120 914 1170 905 1200 895 Z" fill="#cadeef" opacity=".9"/>
  <path d="M0 330 C80 300 170 300 250 340" fill="none" stroke="#7bb3de" stroke-width="1.5" opacity=".6"/>
</svg>
<svg class="abs" style="left:560px;top:1860px" width="560" height="440" viewBox="0 0 560 440" role="img" aria-label="Woman in a blue dress walking past washers beneath a neon laundromat sign">
  <defs><linearGradient id="dryPhoto" x1="0" y1="0" x2="1" y2="1"><stop offset="0" stop-color="#b7d4ea"/><stop offset=".5" stop-color="#e4e1d8"/><stop offset="1" stop-color="#9fb3c4"/></linearGradient></defs>
  <circle cx="262" cy="220" r="212" fill="#2a70c4" opacity=".5"/>
  <path d="M258 20 C370 20 460 110 460 220 C460 330 370 410 260 410 C180 410 110 390 60 400 C30 340 0 280 20 210 C40 100 140 20 258 20 Z" fill="url(#dryPhoto)"/>
  <path d="M496 130 C530 130 552 156 548 188 C544 216 520 230 494 226 C484 238 470 246 452 248 C466 236 470 222 466 210 C450 196 444 176 452 158 C460 140 476 130 496 130 Z" fill="#19c6f5"/>
</svg>
<h3 class="abs heading service-title" style="left:86px;top:2090px;color:#fff">Dry Cleaning Service</h3>
<div class="abs sub" style="left:88px;top:2132px;color:#fff">A Full Service Laundromat</div>
<p class="abs para service-body" style="left:88px;top:2164px;color:#fff">Lorem quis bibendum auctor nisi elit consequat ipsum nec sagittis sem nibh id elit. Duis sed odio sit amet nibh vulputate cursus a sit amet mauris morbi accumsan ipsum velit nam nec tellus a tincidunt...</p>
<a class="btn btn-white" style="left:92px;top:2276px;width:132px;height:40px">Read More</a>

<!-- professional laundry -->
<svg class="abs" style="left:84px;top:2536px" width="560" height="470" viewBox="0 0 560 470" aria-hidden="true">
  <path d="M300 465 C180 470 40 420 22 290 C40 370 140 440 270 448 Z" fill="#eceeef"/>
  <g fill="#d5d8dc">
    <circle cx="444" cy="90" r="4"/><circle cx="470" cy="90" r="4"/><circle cx="496" cy="90" r="4"/>
    <circle cx="444" cy="116" r="4"/><circle cx="470" cy="116" r="4"/><circle cx="496" cy="116" r="4"/>
    <circle cx="444" cy="142" r="4"/><circle cx="470" cy="142" r="4"/><circle cx="496" cy="142" r="4"/>
    <circle cx="496" cy="168" r="4"/>
  </g>
</svg>
<svg class="abs" style="left:84px;top:2536px" width="560" height="470" viewBox="0 0 560 470" role="img" aria-label="Portrait in profile of a woman with red curled hair in front of a washer">
  <defs><linearGradient id="proPhoto" x1="0" y1="0" x2="1" y2="1"><stop offset="0" stop-color="#c46a3c"/><stop offset=".45" stop-color="#8a4a2e"/><stop offset=".7" stop-color="#2c6fc2"/><stop offset="1" stop-color="#d9dbd8"/></linearGradient></defs>
  <path d="M260 4 C400 20 500 120 520 240 C535 320 545 380 545 440 C520 400 470 400 420 415 C380 432 330 440 270 438 C155 438 60 350 56 240 C52 120 140 -8 260 4 Z" fill="url(#proPhoto)"/>
  <path d="M44 160 C80 154 108 180 104 216 C100 245 76 260 46 256 C36 270 20 278 4 280 C16 268 22 254 18 240 C2 226 -4 200 8 182 C16 168 28 162 44 160 Z" fill="#19c6f5"/>
</svg>
<h3 class="abs heading service-title" style="left:710px;top:2672px">Professional Laundry</h3>
<div class="abs sub" style="left:712px;top:2714px">A Full Service Laundromat</div>
<p class="abs para service-body" style="left:712px;top:2748px">Lorem quis bibendum auctor nisi elit consequat ipsum nec sagittis sem nibh id elit. Duis sed odio sit amet nibh vulputate cursus a sit amet mauris morbi accumsan ipsum velit nam nec tellus a tincidunt...</p>
<a class="btn btn-outline" style="left:716px;top:2860px;width:134px;height:40px">Read More</a>

<div class="abs divider" style="top:3083px"></div>

<!-- testimonials -->
<h2 class="abs heading reviews-title">Our Customers Love Our Services</h2>

<div class="review" style="left:90px">
  <div class="avatar" role="img" aria-label="Customer portrait"></div>
  <div class="quote">&ldquo;&ldquo;</div>
  <p class="review-text">Eaque laudantium et beatae nobis accusamus in harum. Impedit ieaque aperiam provident..</p>
  <div class="reviewer">Marcus Hale</div>
  <div class="reviewer-place">At atlanta</div>
  <div class="stars"><svg width="98" height="16" viewBox="0 0 98 16"><g fill="#f3b431"><path id="st" d="M8 0 L10 5.6 L16 6 L11.4 9.8 L13 16 L8 12.6 L3 16 L4.6 9.8 L0 6 L6 5.6 Z"/><use href="#st" x="20"/><use href="#st" x="40"/><use href="#st" x="60"/></g><use href="#st" x="80" fill="#f7d98e"/></svg></div>
</div>
<div class="review" style="left:436px">
  <div class="avatar" role="img" aria-label="Customer portrait"></div>
  <div class="quote">&ldquo;&ldquo;</div>
  <p class="review-text">Eaque laudantium et beatae nobis accusamus in harum. Impedit ieaque aperiam provident..</p>
  <div class="reviewer">Marcus Hale</div>
  <div class="reviewer-place">At atlanta</div>
  <div class="stars"><svg width="98" height="16" viewBox="0 0 98 16"><g fill="#f3b431"><use href="#st"/><use href="#st" x="20"/><use href="#st" x="40"/><use href="#st" x="60"/></g><use href="#st" x="80" fill="#f7d98e"/></svg></div>
</div>
<div class="review" style="left:782px">
  <div class="avatar" role="img" aria-label="Customer portrait"></div>
  <div class="quote">&ldquo;&ldquo;</div>
  <p class="review-text">Eaque laudantium et beatae nobis accusamus in harum. Impedit ieaque aperiam provident..</p>
  <div class="reviewer">Marcus Hale</div>
  <div class="reviewer-place">At Atlanta</div>
  <div class="stars"><svg width="98" height="16" viewBox="0 0 98 16"><g fill="#f3b431"><use href="#st"/><use href="#st" x="20"/><use href="#st" x="40"/><use href="#st" x="60"/></g><use href="#st" x="80" fill="#f7d98e"/></svg></div>
</div>

<!-- footer waves -->
<svg class="abs" style="left:0;top:3590px" width="1200" height="670" viewBox="0 0 1200 670" aria-hidden="true">
  <path d="M0 10 C80 20 160 60 230 110 C300 160 330 210 420 230 C600 270 760 210 900 150 C1020 100 1120 110 1200 120 L1200 670 L0 670 Z" fill="#0b4899"/>
  <path d="M0 10 C90 22 170 60 230 110 C160 70 80 40 0 30 Z" fill="#19c6f5"/>
  <path d="M360 210 C430 245 520 262 620 250 C540 270 450 268 380 240 Z" fill="#19c6f5"/>
  <path d="M900 150 C1000 100 1100 92 1200 100 L1200 115 C1110 108 1010 118 900 150 Z" fill="#19c6f5"/>
  <line x1="88" y1="610" x2="1112" y2="610" stroke="rgba(255,255,255,.2)"/>
</svg>

<div class="abs cta-box">
  <div class="cta-text">Book our laundry services<br>&amp; get 30% discount</div>
  <a class="btn btn-white" style="left:568px;top:66px;width:132px;height:40px">Order Now</a>
</div>

<div class="brand" style="left:88px;top:3990px;font-size:40px;color:#fff"><span class="brand-dot" style="width:14px;height:14px;background:#fff"></span>Suds Harbor</div>

<div class="abs footer-head" style="left:393px;top:3908px">Quick Links</div>
<ul class="abs footer-links" style="left:393px;top:3962px">
  <li>Home</li><li>About Us</li><li>Our Services</li><li>Locations</li><li>Reviews</li><li>Contact Us</li>
</ul>

<div class="abs footer-head" style="left:568px;top:3908px">Contact Info</div>
<svg class="abs" style="left:568px;top:3962px" width="14" height="10" viewBox="0 0 14 10" aria-hidden="true"><rect width="14" height="10" rx="1" fill="#19c6f5"/><path d="M0 1 L7 6 L14 1" stroke="#0b4899" fill="none" stroke-width="1.2"/></svg>
<div class="abs footer-small" style="left:591px;top:3954px">Email:<br>hello@sudsharbor-example.com</div>
<svg class="abs" style="left:568px;top:4020px" width="13" height="13" viewBox="0 0 13 13" aria-hidden="true"><path d="M2 0 L5 3 L3.5 5 C4.5 7 6 8.5 8 9.5 L10 8 L13 11 L11 13 C5 12 1 8 0 2 Z" fill="#19c6f5"/></svg>
<div class="abs footer-small" style="left:591px;top:4010px">Phone:<br>+14045550182</div>
<svg class="abs" style="left:570px;top:4076px" width="11" height="15" viewBox="0 0 11 15" aria-hidden="true"><path d="M5.5 0 C8.5 0 11 2.4 11 5.4 C11 9 5.5 15 5.5 15 C5.5 15 0 9 0 5.4 C0 2.4 2.5 0 5.5 0 Z" fill="#19c6f5"/><circle cx="5.5" cy="5.4" r="2" fill="#0b4899"/></svg>
<div class="abs footer-small" style="left:591px;top:4068px">Office Location:<br>2210 Maple Row NE #12,<br>Atlanta, GA 30300</div>

<div class="abs footer-head" style="left:850px;top:3908px">Newsletter</div>
<div class="abs footer-small" style="left:851px;top:3956px;width:240px;line-height:18px">Subscribe to our email address to get the latest news.</div>
<div class="abs news-input">
  <svg class="abs" style="left:16px;top:16px" width="12" height="9" viewBox="0 0 12 9" aria-hidden="true"><rect width="12" height="9" rx="1" fill="#b8bcc4"/><path d="M0 1 L6 5 L12 1" stroke="#fff" fill="none"/></svg>
  <span>Enter Your Email...</span>
  <div class="news-send"><svg width="16" height="16" viewBox="0 0 16 16"><path d="M0 7 L16 0 L12 16 L7 10 Z" fill="#fff"/></svg></div>
</div>
<div class="abs social" style="left:852px;top:4076px"></div>
<div class="abs social" style="left:894px;top:4076px"></div>
<div class="abs social" style="left:936px;top:4076px"></div>
<div class="abs social" style="left:977px;top:4076px"></div>

<div class="abs copyright">© COPYRIGHT 2021 &nbsp;|&nbsp; ALL RIGHTS RESERVED</div>
<div class="abs to-top"><svg width="10" height="12" viewBox="0 0 10 12"><path d="M5 1 L5 12 M1 5 L5 1 L9 5" stroke="#0b4899" stroke-width="1.4" fill="none"/></svg></div>

</div>
</body>
</html>
```